Web Design Project

We need a design for the actual web.
http://mirela.vunto.example/
It will be a cakes and cupcakes online shop.

It is a one page site, with five anchors.

Inicio (Home)
Here it will show a brief explanation about our shop, just explaining we sell really nice cakes and cupcakes. Also we want to show a slide gallery, like the one it is working, but with not nice choosen pictures.

Productos/Tortas
This two anchors will be just one at the end, but I wanted to show the two options for accessing the different products, tabs or buttons. You can click on the firsts images on that links for see the "pop up image" with a better explanation of every product.

Contacto
Here it will show a little form, that will only appear in smartphones and maybe tablets, this form needs to be similar and much more simple than the principal form (the next anchor), so just focus on it once the next one its done.

Form
This will be the way the users will send the orders, its a complex form, focused on the UX. We dont want the user to type too much and we want it to surprise the user and fell really comfortable.

Industry/Entity Type

Tv

Requirements
Must have

• -Must have side menu, but you can redesign it completelly, but with the same structure
-Its important to focus all the content in the top and middle, we arent sure about users screens and it we set info at the footer, maybe its not gonna show (no scroll vertical).
-You can change all the colours of the site, we are open to new visions, you can surprise us.

```html
<!DOCTYPE html>
<html lang="es">
<head>
<meta charset="utf-8">
<title>Pomeli — Pastelería artesanal</title>
<link href="https://fonts.googleapis.com/css2?family=Pacifico&family=Fredoka:wght@600&family=Arimo:wght@400;700&display=swap" rel="stylesheet">
<style>
  :root {
    --page-bg: #f7e9a6;
    --column-bg: #fff9d2;
    --column-edge: #fdf3c0;
    --navy: #0f2357;
    --teal: #0e8f8a;
    --teal-dark: #06625f;
    --teal-light: #18b3ac;
    --text-grey: #4d5458;
    --muted: #a09a84;
    --slide-blue: #dceef6;
    --white: #ffffff;
  }
  * { margin: 0; padding: 0; box-sizing: border-box; }
  html, body { width: 1200px; height: 478px; overflow: hidden; }
  body {
    background: var(--page-bg);
    font-family: "Arimo", Arial, sans-serif;
    position: relative;
  }
  .site-column {
    position: absolute; left: 150px; top: 0; width: 900px; height: 478px;
    background: linear-gradient(to bottom, var(--column-bg), var(--column-edge));
    box-shadow: 0 0 14px rgba(170, 150, 70, .25);
  }
  .header-photo {
    position: absolute; left: 342px; top: 0; width: 213px; height: 170px;
    background: radial-gradient(ellipse at 50% 25%, #8fe3ea 0%, #6fd3de 35%, #f4e6cc 62%, rgba(255,249,210,0) 80%);
  }
  .brand {
    position: absolute; left: 234px; top: 26px;
    font-family: "Arimo", Arial, sans-serif;
  }
  .brand-name {
    display: block; font-size: 32px; line-height: 36px;
    font-weight: 700; color: var(--teal-dark); letter-spacing: .5px;
  }
  .brand-tagline {
    display: block; margin-top: 4px;
    font-size: 12px; font-weight: 400; color: var(--text-grey); letter-spacing: 1px;
  }
  .social {
    position: absolute; left: 817px; top: 37px;
    display: flex; align-items: center;
  }
  .social-label { font-size: 10px; color: var(--muted); margin-right: 18px; }
  .social-square { width: 37px; height: 37px; border-radius: 2px; margin-right: 20px; box-shadow: 0 1px 2px rgba(0,0,0,.2); }
  .social-square.one { background: #3d5a98; }
  .social-square.two { background: #1ca6df; }

  .main-nav { position: absolute; left: 169px; top: 109px; width: 862px; height: 51px; }
  .nav-band { position: absolute; left: 0; top: 0; }
  .nav-list {
    position: absolute; left: 42px; top: 3px; width: 778px; height: 44px;
    display: flex; list-style: none;
  }
  .nav-item {
    flex: 1; display: flex; align-items: center; justify-content: center;
    font-family: "Fredoka", "Arial Rounded MT Bold", sans-serif; font-weight: 600;
    font-size: 14px; color: var(--white); letter-spacing: .3px;
    text-shadow: 0 1px 1px rgba(0,0,0,.45);
    border-left: 1px solid rgba(255,255,255,.16);
  }
  .nav-item:first-child { border-left: none; color: #fff6b8;
    background: radial-gradient(ellipse at 50% 50%, rgba(40,200,195,.8), rgba(40,200,195,0) 70%); }
  .nav-icon { margin-right: 8px; flex: none; }

  .slider {
    position: absolute; left: 169px; top: 178px; width: 862px; height: 281px;
    background: linear-gradient(to right, #f1ede2 0%, #eceae3 45%, var(--slide-blue) 62%, #d6ecf5 100%);
    overflow: hidden;
  }
  .slide-photo {
    position: absolute; left: 0; top: 0; width: 490px; height: 281px;
    background: radial-gradient(ellipse at 35% 55%, #f5dcc8 0%, #e9d8c6 30%, #b9d6db 52%, rgba(230,232,226,0) 85%);
  }
  .slide-copy { position: absolute; left: 459px; top: 12px; width: 400px; }
  .slide-title {
    font-family: "Pacifico", cursive; font-weight: 400; color: var(--navy);
    font-size: 33px; line-height: 42px;
  }
  .slide-title span { display: block; margin-left: 30px; }
  .slide-text { margin-top: 20px; font-size: 11.8px; line-height: 17px; color: var(--text-grey); }
  .slide-text p { margin-bottom: 7px; }
  .slide-text strong { color: var(--teal); }
  .slide-button {
    position: absolute; left: 460px; top: 233px; display: flex; align-items: center;
  }
  .slide-dots { position: absolute; left: 194px; top: 254px; display: flex; gap: 9px; }
  .dot { width: 7px; height: 7px; border-radius: 50%; background: var(--white); }
  .dot.active { width: 10px; height: 10px; margin-top: -1.5px; background: #f3eab5; }
</style>
</head>
<body>
  <div class="site-column">
    <div class="header-photo" role="img" aria-label="Photo of a cupcake with turquoise frosting"></div>
  </div>

  <div class="brand">
    <span class="brand-name">Pomeli</span>
    <span class="brand-tagline">Pastelería artesanal</span>
  </div>

  <div class="social">
    <span class="social-label">Join us:</span>
    <span class="social-square one" role="img" aria-label="Social network link"></span>
    <span class="social-square two" role="img" aria-label="Social network link"></span>
  </div>

  <nav class="main-nav">
    <svg class="nav-band" width="862" height="51" viewBox="0 0 862 51">
      <defs>
        <linearGradient id="navBand" x1="0" y1="0" x2="0" y2="1">
          <stop offset="0" stop-color="#18b3ac"/>
          <stop offset="1" stop-color="#06625f"/>
        </linearGradient>
      </defs>
      <polygon points="0,0 42,0 42,47 0,47 12,23" fill="#0e8f8a"/>
      <polygon points="862,0 820,0 820,47 862,47 850,23" fill="#0e8f8a"/>
      <polygon points="30,47 42,47 42,51" fill="#06625f"/>
      <polygon points="832,47 820,47 820,51" fill="#06625f"/>
      <rect x="42" y="3" width="778" height="44" fill="url(#navBand)"/>
      <rect x="42" y="3" width="778" height="3" fill="#057370"/>
      <rect x="42" y="47" width="778" height="4" fill="#045553"/>
    </svg>
    <ul class="nav-list">
      <li class="nav-item">
        <svg class="nav-icon" width="13" height="11" viewBox="0 0 13 11"><path d="M6.5 0 L13 5.5 H11 V11 H8 V7.5 H5 V11 H2 V5.5 H0 Z" fill="#fff6b8"/></svg>INICIO
      </li>
      <li class="nav-item">PRODUCTOS</li>
      <li class="nav-item">TORTAS</li>
      <li class="nav-item">CONTACTO</li>
      <li class="nav-item">FORM</li>
    </ul>
  </nav>

  <section class="slider">
    <div class="slide-photo" role="img" aria-label="Photo of frosted cupcakes beside a gift tag and a small cherub figure"></div>
    <div class="slide-copy">
      <h1 class="slide-title">Los majones Cupcakes<span>y Pasteles de Santiago</span></h1>
      <div class="slide-text">
        <p>Finalmente ya está disponible en <strong>Santiago de Chile</strong> nuestro catálogo de sabrosos Cupcakes y Tortas.</p>
        <p>Con ingredientes <strong>100% naturales</strong> y elaborados artesanalmente .</p>
        <p>No solo hay que tener en cuenta la <strong>presentación fabulosa</strong> de los mismos, lo que más destacan nuestros clientes es el sabor exquisito y la textura.</p>
      </div>
    </div>
    <a class="slide-button" href="http://mirela.vunto.example/">
      <svg width="153" height="29" viewBox="0 0 153 29">
        <defs>
          <linearGradient id="btnFill" x1="0" y1="0" x2="0" y2="1">
            <stop offset="0" stop-color="#18b3ac"/>
            <stop offset="1" stop-color="#06625f"/>
          </linearGradient>
        </defs>
        <polygon points="0,0 139,0 153,14.5 139,29 0,29" fill="url(#btnFill)"/>
        <text x="10" y="18.5" font-family="Arimo, Arial, sans-serif" font-weight="700" font-size="11.5" fill="#ffffff">View all our products</text>
        <polygon points="138,11 142,14.5 138,18" fill="#ffffff"/>
      </svg>
    </a>
    <div class="slide-dots">
      <span class="dot"></span><span class="dot active"></span><span class="dot"></span><span class="dot"></span>
    </div>
  </section>
</body>
</html>
```